Create a powerful circular diagram to get the message accross

I need a diagram designed that demonstrates the power of our service by showing the limitations of all our competitors. All the data is provided it just needs to be illustrated.

Target Market(s)

People who work in all the categories listed, we are trying to show them why Open Path Renewal is better than the rest

Font styles to use
Sans Serif

Requirements
Must have
• You need to create one big wheel that groups together all the of the modailties listed according to their colors. So for example you can have all the modalities that only have the red color underneath and put them all under one group. Some modalities have two or three colors you can only group them with modlities with the exact same number of colors and type of colors. The idea is to show that Open Path renewal is the only modality that covers all color fields (ie: color catagories of physical, mental, emotional etc.
• It must have te OPR logo and the lumawell ventures logo on it
• it must have the web address
• www.lumawell-example.com.au on it
• you cannot leave anything out all modalities and fields must be included.
• Must match the Lumawell Blue and the lumawell font
Nice to have
• i would love to see you use your creativity :)
Should not have
• Limit the amount of black, have a look at www.lumawell-example.com.au for brand colors

```html
<!DOCTYPE html>
<html lang="en">
<head>
<meta charset="utf-8">
<title>Open Path Renewal – Healing Wheel</title>
<link href="https://fonts.googleapis.com/css2?family=Poppins:ital,wght@0,500;0,600;0,700;1,500;1,600&family=PT+Serif:ital,wght@1,700&display=swap" rel="stylesheet">
<style>
  :root {
    --brand-blue: #0a88cf;
    --link-blue: #1a6fc0;
    --ink: #1d1d1f;
    --white: #ffffff;
    --physical: #ec1c34;
    --mental: #00ade1;
    --emotional: #39b54a;
    --energetic: #f47b20;
    --subconscious: #e8b521;
    --superconscious: #7b52a3;
    --testing: #d4479a;
  }
  * { margin: 0; padding: 0; box-sizing: border-box; }
  html, body { width: 1200px; height: 734px; overflow: hidden; background: var(--white); }
  .canvas {
    position: relative; width: 1200px; height: 734px;
    background: var(--brand-blue);
    font-family: "Poppins", sans-serif;
  }
  .sheet {
    position: absolute; left: 17px; top: 17px; right: 17px; bottom: 17px;
    background: var(--white);
  }
  .brand-mark {
    position: absolute; left: 52px; top: 36px;
    display: flex; align-items: center; gap: 12px;
  }
  .brand-mark__circle {
    width: 64px; height: 64px; border-radius: 50%;
    border: 2.5px solid var(--brand-blue);
  }
  .brand-mark__name {
    font-size: 28px; font-weight: 500; color: var(--brand-blue); white-space: nowrap;
  }
  .web-address {
    position: absolute; left: 448px; top: 43px; width: 316px; height: 46px;
    border: 1.5px solid var(--brand-blue); border-radius: 23px;
    display: flex; align-items: center; justify-content: center;
    font-family: "PT Serif", serif; font-style: italic; font-weight: 700;
    font-size: 20px; color: var(--brand-blue); white-space: nowrap;
  }
  .partner-mark {
    position: absolute; right: 62px; top: 48px;
    font-size: 27px; font-weight: 500; color: var(--brand-blue); white-space: nowrap;
  }
  .claims {
    position: absolute; left: 28px; top: 150px; width: 503px; height: 156px;
    background: var(--brand-blue); border-radius: 40px;
    list-style: none; padding: 24px 0 0 37px;
    color: var(--white); font-size: 14.4px; font-weight: 500; line-height: 18px;
  }
  .claims li { position: relative; padding-left: 11px; margin-bottom: 7.6px; white-space: nowrap; }
  .claims li::before {
    content: ""; position: absolute; left: -8px; top: 6px;
    width: 6px; height: 6px; background: var(--white); transform: rotate(45deg);
  }
  .fields {
    position: absolute; left: 62px; top: 336px;
    font-style: italic; white-space: nowrap;
  }
  .fields dt {
    font-size: 14.8px; font-weight: 600; color: var(--ink); line-height: 16px;
    text-transform: uppercase;
  }
  .fields dd {
    font-size: 12.8px; font-weight: 500; color: var(--link-blue);
    line-height: 15.8px; margin-bottom: 5.6px;
  }
  .wheel { position: absolute; left: 566px; top: 88px; width: 600px; height: 600px; }
  .wheel text { font-family: "Poppins", sans-serif; fill: var(--white); text-anchor: middle; }
  .wheel .field-label { font-size: 21px; font-weight: 600; letter-spacing: 0.6px; }
  .wheel .field-label--small { font-size: 15px; }
  .wheel .group-title { font-size: 23px; font-weight: 700; }
  .wheel .group-title--large { font-size: 25px; }
  .wheel .modality { font-size: 8.4px; font-weight: 600; }
  .wheel .modality--compact { font-size: 8px; font-weight: 600; }
  .wheel .modality--tight { font-size: 7.5px; }
  .wheel .modality--large { font-size: 10.5px; font-weight: 600; }
  .seg { stroke: var(--white); stroke-width: 4; stroke-linejoin: round; }
</style>
</head>
<body>
<div class="canvas">
  <div class="sheet"></div>

  <div class="brand-mark">
    <div class="brand-mark__circle"></div>
    <span class="brand-mark__name">Open Path Renewal</span>
  </div>

  <div class="web-address">www.lumawell-example.com.au</div>

  <div class="partner-mark">lumawell ventures</div>

  <ul class="claims">
    <li>OPR is the only modality that empowers you to heal yourself.</li>
    <li>OPR is the only modality that enables you to heal on all levels<br>simultaneously.</li>
    <li>OPR is the only modality that incorporates emotional<br>processing in the body for a whole of self healing.</li>
  </ul>

  <dl class="fields">
    <dt>Phyisical</dt>
    <dd>To heal the physical i must have a physical experience.</dd>
    <dt>Mental</dt>
    <dd>To heal mentally my conscious mind must be engaged.</dd>
    <dt>Emotional</dt>
    <dd>To heal emotionally my emotions must be explored and experienced.</dd>
    <dt>Energetic</dt>
    <dd>To heal energetically, i must have an experience of energy moving in my body.</dd>
    <dt>Subconscious</dt>
    <dd>To heal my subconscious I must access it and engage with it.</dd>
    <dt>Superconsious</dt>
    <dd>To heal my superconscious mind i must experience clarity or wisdom<br>(epiphanies) from my higher self.</dd>
    <dt>Before &amp; After Testing</dt>
    <dd>For my healing to be conclusive before &amp; after testing must be done during my<br>healing session.</dd>
  </dl>

  <svg class="wheel" viewBox="-300 -300 600 600" aria-label="Healing wheel of modalities grouped by field">
    <defs>
      <path id="ring-cw" d="M0 258 A258 258 0 1 1 0 -258 A258 258 0 1 1 0 258"/>
      <path id="ring-cw-outer" d="M0 273 A273 273 0 1 1 0 -273 A273 273 0 1 1 0 273"/>
      <path id="ring-cw-inner" d="M0 255 A255 255 0 1 1 0 -255 A255 255 0 1 1 0 255"/>
      <path id="ring-ccw" d="M0 -275 A275 275 0 1 0 0 275 A275 275 0 1 0 0 -275"/>
      <radialGradient id="portrait-tone" cx="50%" cy="40%" r="60%">
        <stop offset="0%" stop-color="#e6e6e6"/>
        <stop offset="100%" stop-color="#8f8f8f"/>
      </radialGradient>
    </defs>

    <g class="field-bands">
      <path class="seg" fill="var(--physical)" d="M-118.8 -266.7 A292 292 0 0 1 123.4 -264.6 L101.8 -218.4 A241 241 0 0 0 -98.0 -220.2 Z"/>
      <path class="seg" fill="var(--mental)" d="M123.4 -264.6 A292 292 0 0 1 284.5 -65.7 L234.8 -54.2 A241 241 0 0 0 101.8 -218.4 Z"/>
      <path class="seg" fill="var(--emotional)" d="M284.5 -65.7 A292 292 0 0 1 223.7 187.7 L184.6 154.9 A241 241 0 0 0 234.8 -54.2 Z"/>
      <path class="seg" fill="var(--energetic)" d="M223.7 187.7 A292 292 0 0 1 0 292 L0 241 A241 241 0 0 0 184.6 154.9 Z"/>
      <path class="seg" fill="var(--subconscious)" d="M0 292 A292 292 0 0 1 -223.7 187.7 L-184.6 154.9 A241 241 0 0 0 0 241 Z"/>
      <path class="seg" fill="var(--superconscious)" d="M-223.7 187.7 A292 292 0 0 1 -284.5 -65.7 L-234.8 -54.2 A241 241 0 0 0 -184.6 154.9 Z"/>
      <path class="seg" fill="var(--testing)" d="M-284.5 -65.7 A292 292 0 0 1 -118.8 -266.7 L-98.0 -220.2 A241 241 0 0 0 -234.8 -54.2 Z"/>
    </g>

    <g class="modality-groups">
      <path class="seg" fill="var(--physical)" d="M-96.0 -215.6 A236 236 0 0 1 99.7 -213.9 L35.9 -77.0 A85 85 0 0 0 -34.6 -77.6 Z"/>
      <path class="seg" fill="var(--mental)" d="M99.7 -213.9 A236 236 0 0 1 230.0 -53.1 L82.8 -19.1 A85 85 0 0 0 35.9 -77.0 Z"/>
      <path class="seg" fill="var(--emotional)" d="M230.0 -53.1 A236 236 0 0 1 180.8 151.7 L65.1 54.6 A85 85 0 0 0 82.8 -19.1 Z"/>
      <path class="seg" fill="var(--energetic)" d="M180.8 151.7 A236 236 0 0 1 0 236 L0 85 A85 85 0 0 0 65.1 54.6 Z"/>
      <path class="seg" fill="var(--subconscious)" d="M0 236 A236 236 0 0 1 -180.8 151.7 L-65.1 54.6 A85 85 0 0 0 0 85 Z"/>
      <path class="seg" fill="var(--superconscious)" d="M-180.8 151.7 A236 236 0 0 1 -230.0 -53.1 L-82.8 -19.1 A85 85 0 0 0 -65.1 54.6 Z"/>
      <path class="seg" fill="var(--testing)" d="M-230.0 -53.1 A236 236 0 0 1 -96.0 -215.6 L-34.6 -77.6 A85 85 0 0 0 -82.8 -19.1 Z"/>
    </g>

    <circle cx="0" cy="0" r="83" fill="var(--white)"/>
    <g class="hub-ring" fill="none" stroke-width="4">
      <circle r="70" pathLength="360" stroke="var(--testing)" stroke-dasharray="45 315" transform="rotate(-163)"/>
      <circle r="70" pathLength="360" stroke="var(--physical)" stroke-dasharray="41 319" transform="rotate(-110)"/>
      <circle r="70" pathLength="360" stroke="var(--mental)" stroke-dasharray="44 316" transform="rotate(-61)"/>
      <circle r="70" pathLength="360" stroke="var(--emotional)" stroke-dasharray="45 315" transform="rotate(-9)"/>
      <circle r="70" pathLength="360" stroke="var(--energetic)" stroke-dasharray="42 318" transform="rotate(44)"/>
      <circle r="70" pathLength="360" stroke="var(--subconscious)" stroke-dasharray="42 318" transform="rotate(94)"/>
      <circle r="70" pathLength="360" stroke="var(--superconscious)" stroke-dasharray="45 315" transform="rotate(144)"/>
    </g>
    <g role="img" aria-label="Portrait illustration of a woman at the centre of the wheel">
      <circle r="60" fill="url(#portrait-tone)"/>
    </g>

    <text class="field-label"><textPath href="#ring-cw" startOffset="50%">PHYSICAL</textPath></text>
    <text class="field-label"><textPath href="#ring-cw" startOffset="64.2%">MENTAL/CONSIOUS</textPath></text>
    <text class="field-label field-label--small"><textPath href="#ring-cw-outer" startOffset="36.1%">BEFORE &amp; AFTER</textPath></text>
    <text class="field-label field-label--small"><textPath href="#ring-cw-inner" startOffset="36.8%">TESTING</textPath></text>
    <text class="field-label"><textPath href="#ring-ccw" startOffset="71.4%">EMOTIONAL</textPath></text>
    <text class="field-label"><textPath href="#ring-ccw" startOffset="56.9%">ENERGETIC</textPath></text>
    <text class="field-label"><textPath href="#ring-ccw" startOffset="43.1%">SUBCONSCIOUS</textPath></text>
    <text class="field-label"><textPath href="#ring-ccw" startOffset="28.9%">SUPERCONSCIOUS</textPath></text>

    <!-- physical group -->
    <text class="group-title" x="0" y="-215">OPR</text>
    <text class="modality--compact">
      <tspan x="0" y="-203.5">MASSAGE , YOGA , CHINESE MEDICINE</tspan>
      <tspan x="0" y="-192.5">CHIRO-PRACTIC , KINESIOLOGY</tspan>
      <tspan x="0" y="-181.5">NATROPATHY</tspan>
      <tspan x="0" y="-170.5">NUTRITIONAL HEALING</tspan>
      <tspan x="0" y="-159.5">ACCUPUNC-TURE</tspan>
      <tspan x="0" y="-148.5">BOWEN THERAPY</tspan>
      <tspan class="modality--tight" x="0" y="-137.8">PSYCHIC INTUITIVE</tspan>
      <tspan class="modality--tight" x="0" y="-127.8">FAMILY-CONSTELLATION</tspan>
      <tspan class="modality--tight" x="0" y="-117.8">AYURVEDIC MEDICINE</tspan>
      <tspan class="modality--tight" x="0" y="-107.8">WESTERN MEDICINE</tspan>
      <tspan class="modality--tight" x="0" y="-96.5">EFT</tspan>
    </text>

    <!-- mental group -->
    <text class="group-title" x="135.5" y="-159">OPR</text>
    <text class="modality">
      <tspan x="135.5" y="-148.5">PSHYCHOLOGY</tspan>
      <tspan x="135.5" y="-136.6">LIFE COACHING</tspan>
      <tspan x="135.5" y="-125.9">MINDFULLNESS MEDITATION</tspan>
      <tspan x="135.5" y="-114.6">HYPNO-THERAPY</tspan>
      <tspan x="135.5" y="-102.7">TIMELINE THERAPY</tspan>
      <tspan x="135.5" y="-91.4">INNER CHILD HEALING</tspan>
      <tspan x="135.5" y="-79.6">PSYCHIC INTUITIVE</tspan>
      <tspan x="135.5" y="-68.3">FAMILY-CONSTELLATION</tspan>
      <tspan x="135.5" y="-56.4">NLP</tspan>
      <tspan x="135.5" y="-44.6">EFT</tspan>
    </text>

    <!-- testing group -->
    <text class="group-title" x="-131.5" y="-157">OPR</text>
    <text class="modality">
      <tspan x="-131.5" y="-144.5">CHINESE MEDICINE</tspan>
      <tspan x="-131.5" y="-133.2">CHIRO-PRACTIC</tspan>
      <tspan x="-131.5" y="-121.4">KINESIOLOGY</tspan>
      <tspan x="-131.5" y="-110.1">NUTRITIONAL HEALING</tspan>
      <tspan x="-131.5" y="-98.2">NLP</tspan>
      <tspan x="-131.5" y="-86.9">BOWEN THERAPY</tspan>
      <tspan x="-131.5" y="-75.1">ENERGY MEDICINE</tspan>
      <tspan x="-131.5" y="-63.2">TIMELINE THERAPY</tspan>
      <tspan x="-131.5" y="-51.9">EFT</tspan>
    </text>

    <!-- superconscious group -->
    <text class="group-title" x="-164.8" y="36">OPR</text>
    <text class="modality--large" x="-164.8" y="49">THETA HEALING</text>

    <!-- emotional group -->
    <text class="group-title group-title--large" x="160.9" y="45">OPR</text>

    <!-- subconscious group -->
    <text class="group-title" x="-69.4" y="114">OPR</text>
    <text class="modality">
      <tspan x="-69.4" y="125.3">KINESIOLOGY</tspan>
      <tspan x="-69.4" y="137.2">NLP</tspan>
      <tspan x="-69.4" y="149">BOWEN THERAPY</tspan>
      <tspan x="-69.4" y="160.3">HYPNO-THERAPY</tspan>
      <tspan x="-69.4" y="172.2">TIMELINE THERAPY</tspan>
      <tspan x="-69.4" y="184">INNER CHILD HEALING</tspan>
      <tspan x="-69.4" y="195.3">THETA HEALING</tspan>
      <tspan x="-69.4" y="207.2">EFT</tspan>
    </text>

    <!-- energetic group -->
    <text class="group-title" x="71.7" y="115.7">OPR</text>
    <text class="modality">
      <tspan x="71.7" y="127.6">CHINESE MEDICINE</tspan>
      <tspan x="71.7" y="139.5">CHIRO-PRACTIC</tspan>
      <tspan x="71.7" y="150.8">REIKI</tspan>
      <tspan x="71.7" y="162.6">ACCUPUNC-TURE</tspan>
      <tspan x="71.7" y="173.9">CRYSTAL HEALING</tspan>
      <tspan x="71.7" y="185.8">ENERGY MEDICINE</tspan>
      <tspan x="71.7" y="197.1">FAMILY-CONSTELLATION</tspan>
    </text>
  </svg>
</div>
</body>
</html>
```